Brivane Redesign

We need a face lift for our website, www.brivane.com. We sell flooring and related products nationwide. We are interested in expanding the width of the website and introducing grays and black. We want the design to be both contemporary and user friendly.

```html
<!DOCTYPE html>
<html lang="en">
<head>
<meta charset="utf-8">
<title>Brivane — Flooring</title>
<link href="https://fonts.googleapis.com/css2?family=Open+Sans:wght@400;600;700&display=swap" rel="stylesheet">
<style>
:root{
  --red:#c0161b;
  --red-dark:#9e0f12;
  --ink:#222;
  --text:#333;
  --muted:#666;
  --line:#dcdcdc;
  --topbar:#efefef;
  --nav:#4a4a4a;
  --nav-dark:#2e2e2e;
  --footer:#3a3a3a;
  --footer-text:#bdbdbd;
  --btn-grey:#ededed;
}
*{box-sizing:border-box;margin:0;padding:0}
html,body{width:986px;height:1200px;overflow:hidden;background:#fff}
body{font-family:'Open Sans',Arial,sans-serif;color:var(--text)}
.page{position:relative;width:986px;height:1200px;overflow:hidden}
.abs{position:absolute}

/* utility bar */
.utility{left:0;top:0;width:986px;height:38px;background:var(--topbar);border-bottom:1px solid var(--line)}
.utility ul{position:absolute;left:82px;top:0;width:823px;height:38px;display:flex;list-style:none;border-left:1px solid #d4d4d4}
.utility li{height:38px;display:flex;align-items:center;justify-content:center;gap:6px;font-size:11.5px;color:#444;border-right:1px solid #d4d4d4;text-transform:uppercase}
.utility li svg{width:11px;height:11px;fill:#444}
.utility .cart{text-transform:none;flex:1}
.utility .cart b{font-weight:400;text-transform:uppercase}

/* header */
.header{left:0;top:38px;width:986px;height:103px;background:linear-gradient(#fff,#f6f6f6)}
.brand{position:absolute;left:83px;top:36px;display:flex;align-items:center;gap:8px}
.brand-mark{width:26px;height:26px;background:var(--red)}
.brand-name{font-size:30px;font-weight:700;color:var(--ink);letter-spacing:-0.5px;line-height:1}
.call{position:absolute;right:103px;top:32px;text-align:right}
.call .lead{font-size:16px;color:var(--ink)}
.call .num{font-size:16px;color:var(--red);font-weight:600}
.call-icon{position:absolute;right:80px;top:38px;width:22px;height:30px}

/* nav */
.nav{left:0;top:141px;width:986px;height:42px;background:linear-gradient(#555,#3c3c3c);border-top:1px solid #2a2a2a}
.nav ul{position:absolute;left:83px;top:0;height:41px;display:flex;list-style:none}
.nav li{height:41px;padding:0 15px;display:flex;align-items:center;color:#fff;font-size:12.5px;font-weight:600;border-right:1px solid #2e2e2e;text-transform:uppercase}
.nav li.active{background:var(--nav-dark)}
.search{position:absolute;left:737px;top:6px;width:165px;height:30px;background:#fff;border:1px solid #ccc;font-size:10.5px;color:#555;padding:8px 12px}
.search svg{position:absolute;right:8px;top:8px;width:13px;height:13px}

/* hero */
.hero{left:0;top:183px;width:986px;height:401px;background:linear-gradient(115deg,#ece9de 0%,#cfd3bf 30%,#6e6a60 47%,#c98a3c 55%,#d79a45 75%,#b86f22 100%)}
.arrow{position:absolute;top:185px;width:30px;height:30px;border-radius:50%;background:#fff;box-shadow:0 1px 3px rgba(0,0,0,.3)}
.arrow svg{width:30px;height:30px}
.caption{position:absolute;left:81px;top:342px;width:823px;height:59px;background:rgba(30,30,30,.85);display:flex;align-items:center;justify-content:center;gap:14px}
.caption p{color:#fff;font-size:19.5px;font-weight:600}
.caption .more{background:#fff;color:#333;font-size:13px;padding:5px 9px;border-radius:2px}

/* feature cards */
.card{top:609px;width:256px}
.card .shot{height:145px}
.card h3{margin:13px 0 0 9px;font-size:14.5px;font-weight:600;color:var(--ink)}
.card .spec{margin:4px 0 0 9px;font-size:12.5px;color:var(--text)}
.card .spec small{font-size:10px}
.card .price{margin:9px 0 0 9px;font-size:12.5px;color:var(--red)}

.rule{left:82px;width:823px;height:1px;background:var(--line)}

.promo-text{left:91px;top:886px;width:572px;font-size:13px;line-height:20px;color:var(--text)}
.promo-btn{left:657px;top:890px;width:240px;height:34px;background:linear-gradient(#c9201f,#a71416);border-radius:3px;color:#fff;font-size:12.5px;font-weight:600;display:flex;align-items:center;justify-content:center;box-shadow:0 1px 2px rgba(0,0,0,.3)}

.quick{top:974px;width:188px;height:41px;background:var(--btn-grey);border:1px solid #d6d6d6;display:flex;align-items:center;justify-content:center;gap:8px;font-size:14.5px;color:#444;font-weight:600;text-transform:uppercase}
.quick i{width:15px;height:15px;border-radius:50%;background:#777;position:relative;display:block}
.quick i::after{content:"";position:absolute;left:5px;top:4px;border-left:5px solid #fff;border-top:3.5px solid transparent;border-bottom:3.5px solid transparent}

.badges{left:82px;top:1050px;width:823px;height:48px;display:flex;align-items:center;justify-content:space-between}
.badge{background:#d9d9d9}
.cards{display:flex;gap:5px}
.cards span{width:36px;height:22px;border-radius:2px;background:#c9c9c9}

/* footer */
.footer{left:0;top:1116px;width:986px;height:84px;background:var(--footer)}
.footer .links{position:absolute;left:83px;top:19px;font-size:11.5px;color:var(--footer-text);word-spacing:2px}
.footer .links span{margin:0 8px;color:#888}
.footer .copy{position:absolute;left:83px;top:49px;font-size:11.5px;color:var(--footer-text)}
.social{position:absolute;left:797px;top:30px;display:flex;gap:9px}
.social span{width:20px;height:20px;border-radius:50%;background:#6a6a6a;display:flex;align-items:center;justify-content:center}
</style>
</head>
<body>
<div class="page">

  <div class="abs utility">
    <ul>
      <li style="width:164px"><svg viewBox="0 0 10 10"><path d="M5 0a3.5 3.5 0 0 0-3.5 3.5C1.5 6 5 10 5 10s3.5-4 3.5-6.5A3.5 3.5 0 0 0 5 0zm0 5a1.5 1.5 0 1 1 0-3 1.5 1.5 0 0 1 0 3z"/></svg>Order Tracking</li>
      <li style="width:84px"><svg viewBox="0 0 10 10"><circle cx="5" cy="5" r="5"/></svg>FAQ</li>
      <li style="width:118px"><svg viewBox="0 0 10 10"><path d="M0 1h10v6H3L1 9V7H0z"/></svg>Live Chat</li>
      <li style="width:141px"><svg viewBox="0 0 10 10"><circle cx="5" cy="3" r="2.6"/><path d="M0 10c0-3 2.2-4.2 5-4.2S10 7 10 10z"/></svg>My Account</li>
      <li class="cart"><svg viewBox="0 0 10 10"><path d="M0 1h2l1.5 5h5L10 2H3"/><circle cx="4" cy="8.5" r="1"/><circle cx="8" cy="8.5" r="1"/></svg><b>My Cart</b>&nbsp;-&nbsp;(0) item(s)&nbsp;in cart&nbsp;&nbsp;&nbsp;Total : $00.00</li>
    </ul>
  </div>

  <header class="abs header">
    <div class="brand"><span class="brand-mark"></span><span class="brand-name">Brivane</span></div>
    <div class="call">
      <div class="lead">Call us Today</div>
      <div class="num">1 - 888 - 555 - 0142</div>
    </div>
    <svg class="call-icon" viewBox="0 0 22 30"><path d="M6 2c-3 1-4 4-3 8 2 7 7 14 13 17 2 1 4 0 5-2l-4-5-3 2c-3-2-5-6-6-10l3-1z" fill="#d0241f"/></svg>
  </header>

  <nav class="abs nav">
    <ul>
      <li class="active">Company</li>
      <li>Products</li>
      <li>Brands</li>
      <li>Home Decor</li>
      <li>Accessories</li>
      <li>Flooring Facts</li>
    </ul>
    <div class="search">Search
      <svg viewBox="0 0 13 13"><circle cx="5" cy="5" r="3.8" fill="none" stroke="#444" stroke-width="1.8"/><path d="M8 8l4 4" stroke="#444" stroke-width="2.2"/></svg>
    </div>
  </nav>

  <section class="abs hero" role="img" aria-label="Modern kitchen with dark tile floor meeting warm honey-toned hardwood flooring">
    <div class="arrow" style="left:83px"><svg viewBox="0 0 30 30"><path d="M17 9l-6 6 6 6" fill="none" stroke="#888" stroke-width="1.5"/></svg></div>
    <div class="arrow" style="left:873px"><svg viewBox="0 0 30 30"><path d="M13 9l6 6-6 6" fill="none" stroke="#888" stroke-width="1.5"/></svg></div>
    <div class="caption">
      <p>Nunc pharetra justo in augue vulputate vestibulum massa.</p>
      <span class="more">Know more</span>
    </div>
  </section>

  <article class="abs card" style="left:83px">
    <div class="shot" role="img" aria-label="Child's feet on a glossy oak hardwood floor" style="background:linear-gradient(135deg,#e0a060,#b8672a 60%,#7a3f18)"></div>
    <h3>Suspendisse potenti</h3>
    <p class="spec">Class aptent taciti&nbsp; - &nbsp;<small>12mm Laminate</small></p>
    <p class="price">Starting @ 2.49 / sq.ft</p>
  </article>
  <article class="abs card" style="left:365px">
    <div class="shot" role="img" aria-label="Dining room with chairs over warm laminate flooring" style="background:linear-gradient(180deg,#d9c6ae,#8a5a35 45%,#c98a50)"></div>
    <h3>Suspendisse potenti</h3>
    <p class="spec">Class aptent taciti&nbsp; - &nbsp;<small>12mm Laminate</small></p>
    <p class="price">Starting @ 2.49 / sq.ft</p>
  </article>
  <article class="abs card" style="left:647px">
    <div class="shot" role="img" aria-label="Sunlit room with light wood floor and window shadows" style="background:linear-gradient(160deg,#6a6458,#b39c74 50%,#8a7652)"></div>
    <h3>Suspendisse potenti</h3>
    <p class="spec">Class aptent taciti&nbsp; - &nbsp;<small>12mm Laminate</small></p>
    <p class="price">Starting @ 2.49 / sq.ft</p>
  </article>

  <div class="abs rule" style="top:861px"></div>
  <p class="abs promo-text">Offering discount prices on laminate, hardwood, cork, bamboo, vinyl and area rugs from the brands you know and trust.</p>
  <div class="abs promo-btn">VIEW OUR CURRENT PROMOTIONS</div>
  <div class="abs rule" style="top:956px"></div>

  <div class="abs quick" style="left:91px"><i></i>Shop by Brand</div>
  <div class="abs quick" style="left:297px"><i></i>Home Decor</div>
  <div class="abs quick" style="left:502px"><i></i>Accessories</div>
  <div class="abs quick" style="left:708px"><i></i>Flooring Facts</div>

  <div class="abs rule" style="top:1033px"></div>

  <div class="abs badges">
    <span class="badge" style="width:60px;height:36px"></span>
    <span class="badge" style="width:108px;height:30px"></span>
    <span class="badge" style="width:46px;height:46px;border-radius:50%"></span>
    <span class="badge" style="width:58px;height:22px"></span>
    <span class="badge" style="width:58px;height:32px"></span>
    <span class="badge" style="width:70px;height:36px"></span>
    <span class="badge" style="width:44px;height:44px;border-radius:50%"></span>
    <span class="cards"><span></span><span></span><span></span><span></span><span></span><span></span></span>
  </div>

  <footer class="abs footer">
    <p class="links">Home<span>|</span>Company<span>|</span>Products<span>|</span>Brands<span>|</span>Home Decor<span>|</span>Accessories<span>|</span>Flooring Facts<span>|</span>Contact us</p>
    <p class="copy">Copyright &nbsp;©&nbsp; 2013 &nbsp;Brivane. &nbsp;All rights reserved.</p>
    <div class="social">
      <span></span><span></span><span></span>
      <span><svg width="11" height="8" viewBox="0 0 11 8"><rect x=".5" y=".5" width="10" height="7" fill="none" stroke="#ddd"/><path d="M.5.5l5 4 5-4" fill="none" stroke="#ddd"/></svg></span>
    </div>
  </footer>

</div>
</body>
</html>
```